Branding for Velēra Cider a new Tasmanian cider company

We are a new Tasmanian cider business looking for a logo/label design to be used on our 330ml cider bottle labels and as a logo.
We want our cider label to pop and stand out from the rest.
As our cider is a Tasmanian product we would like it to appear as a premium product.
I have attached pictures of all of the other Tasmanian Cider labels to give an idea of what we are competing with NOT because we like the designs!!!

We are yet to start advertising our business so it is all an open slab, we have no starting point just a few ideas that have been listed below in the "Nice to Haves" section.

This brief has been updated as what we originally requested was too similar to other labels already in production so didn't give our product an edge.

The label size will be approx 80mm x 125mm

Target Market(s)

Craft cider market, bottle shops, boutique bars and restaurants

Font styles to use
Serif
Decorative
Script

Colors

Designer to choose colors to be used in the design.

Requirements
Must have
• The words
• "Velēra Cider" with the diacritic's over the o's
• "Tasmanian Made"
• or
• "Made in Tasmania"
• The Tasmanian part can be in all caps if it looks better
Nice to have
• All or some of the below incorporated into the label:
• Velēra was the goddess of fruit trees, gardens, and orchards.
• She watched over and protected fruit trees
• She was thought to be a wood nymph which are usually represented as beautiful, young girls.
• We would like our label to possibly incorporate the above.
• Maybe a wood nymph/goddess in an apple/pear orchard or against an apple/pear tree.
• Maybe no tree, just the nymph/goddess holding fruit.
• Maybe an apple/pear branch with a nympy/goddess under it.
• I have attached a few images from searchly of wood nymphs and fruit goddess' for inspiration. Not sure if realistic or animated would look best, but if animated, not cartoon like as we would like a premium look. Possibly similar to the attached Torvik Cider artwork
• We will have 3 types of cider; Apple, Pear and Apple & Strawberry so essentially 3 labels, maybe the apple tree could change to a pear tree and for the apple & strawberry cider maybe strawberries growing under the apple tree?
• All just ideas, we are open to :)
• If you think something else will suit the name, please feel free to submit it

```html
<!DOCTYPE html>
<html lang="en">
<head>
<meta charset="utf-8">
<title>Velēra Cider – Label Concepts</title>
<link rel="stylesheet" href="https://fonts.googleapis.com/css2?family=Source+Sans+3:wght@400;600&display=swap">
<style>
  :root {
    --lime: #b2dc12;
    --lime-text: #a6d11a;
    --white: #ffffff;
    --blush: #fbf6f4;
    --mint-top: #e3f2b3;
    --mint-bottom: #dcefa0;
    --art-light: #b4d84a;
    --art-mid: #8fb52e;
    --art-dark: #5f7a2a;
  }
  * { margin: 0; padding: 0; box-sizing: border-box; }
  html, body {
    width: 1200px;
    height: 1200px;
    overflow: hidden;
    background: var(--white);
  }
  .canvas {
    position: relative;
    width: 1200px;
    height: 1200px;
    background: var(--white);
    font-family: "Source Sans 3", "Myriad Pro", sans-serif;
  }
  .backdrop-band {
    position: absolute;
    left: 0;
    top: 0;
    width: 630px;
    height: 1200px;
    background: var(--lime);
  }
  .label {
    position: absolute;
    top: 307px;
    width: 434px;
    height: 582px;
    text-align: center;
    color: var(--lime-text);
  }
  .label--white { left: 149px; background: var(--white); }
  .label--gradient {
    left: 672px;
    background: linear-gradient(180deg, var(--mint-top) 0%, var(--blush) 30%, var(--blush) 62%, var(--mint-bottom) 100%);
  }
  .fruit-art {
    position: absolute;
    left: 149px;
    top: 86px;
    width: 156px;
    height: 212px;
    background: linear-gradient(180deg, var(--art-light) 0%, var(--art-mid) 60%, var(--art-dark) 100%);
  }
  .brand-name {
    position: absolute;
    left: 0;
    right: 0;
    top: 338px;
    font-size: 46px;
    font-weight: 600;
    letter-spacing: 0.5px;
    line-height: 52px;
  }
  .divider {
    position: absolute;
    left: 25px;
    width: 385px;
    top: 401px;
    height: 2px;
    background: var(--lime-text);
  }
  .origin {
    position: absolute;
    left: 0;
    right: 0;
    top: 418px;
    font-size: 29px;
    font-weight: 400;
    line-height: 34px;
  }
  .volume {
    position: absolute;
    left: 0;
    right: 0;
    top: 518px;
    font-size: 22px;
    font-weight: 400;
    line-height: 26px;
  }
</style>
</head>
<body>
  <main class="canvas">
    <div class="backdrop-band"></div>

    <section class="label label--white">
      <div class="fruit-art" role="img" aria-label="Painted illustration of a green pear"></div>
      <h1 class="brand-name">VELĒRA CIDER</h1>
      <div class="divider"></div>
      <p class="origin">Made in Tasmania</p>
      <p class="volume">330ml</p>
    </section>

    <section class="label label--gradient">
      <div class="fruit-art" role="img" aria-label="Painted illustration of a green pear"></div>
      <h2 class="brand-name">VELĒRA CIDER</h2>
      <div class="divider"></div>
      <p class="origin">Made in Tasmania</p>
      <p class="volume">330ml</p>
    </section>
  </main>
</body>
</html>
```